Australian Recruitment Agency Flyer

We are looking for a 1 page flyer to promote our recruitment company. We would like this to have a corporate look.

Attached is a word document with the content we would like included in the flyer.

I have also attached some of our clients logos to be included in the flyer

Target Market(s)

Professional organisations looking to hire new staff

Industry/Entity Type

It Company

Colors
85abd2
3176b5
31b7a3
d2a4cc
e667a6
b768aa
876aae
3276b5
f04a50

Requirements
Must have
• Must have the content that we have include on a word document in the design brief.

```html
<!DOCTYPE html>
<html lang="en">
<head>
<meta charset="utf-8">
<title>TalentBridge – Recruitment Flyer</title>
<link href="https://fonts.googleapis.com/css2?family=Montserrat:ital,wght@0,300;0,400;0,500;0,600;0,700;0,800;1,300&family=Quicksand:wght@400;500&display=swap" rel="stylesheet">
<style>
  :root{
    --navy:#211c70;
    --navy-deep:#1a1660;
    --blue:#2f40b3;
    --blue-light:#3d55d2;
    --sky:#2ba6e6;
    --cyan:#25b8ec;
    --orange:#f28a1e;
    --paper:#f1f2f5;
    --ink:#1d1d2b;
    --stage:#e8e8ea;
    --white:#ffffff;
  }
  *{box-sizing:border-box;margin:0;padding:0}
  html,body{width:1155px;height:1200px;overflow:hidden;background:var(--stage)}
  .flyer{
    position:absolute;left:167px;top:20px;width:820px;height:1160px;
    overflow:hidden;background:var(--paper);
    font-family:"Quicksand",sans-serif;color:var(--ink);
  }
  .backdrop{position:absolute;inset:0}
  .abs{position:absolute}

  /* brand */
  .brand-mark{left:24px;top:40px;width:70px;height:70px;border-radius:50%;background:var(--orange)}
  .brand-name{left:118px;top:50px;font-family:"Montserrat",sans-serif;font-weight:600;font-size:36px;color:var(--white);letter-spacing:-1px;line-height:1}
  .brand-tag{left:126px;top:100px;font-family:"Montserrat",sans-serif;font-size:13px;font-weight:500;color:var(--white)}

  /* headline */
  .headline{right:18px;top:60px;text-align:right;font-family:"Montserrat",sans-serif;color:var(--white)}
  .headline .lead{font-size:23px;font-weight:400;line-height:1}
  .headline .lead em{font-style:normal;color:var(--cyan)}
  .headline .big{font-size:52px;font-weight:800;color:var(--orange);line-height:1.08;letter-spacing:1px}
  .headline .sub{font-size:22px;font-style:italic;font-weight:300;line-height:1.3;margin-top:4px}

  /* industries */
  .industries{left:85px;top:262px;font-family:"Montserrat",sans-serif;color:var(--white)}
  .industries h2{font-size:20px;font-weight:500;line-height:1.1}
  .industries h2 span{display:block;font-size:32px;font-weight:800;color:var(--orange)}
  .industries .rule{width:165px;height:1px;background:rgba(255,255,255,.55);margin-top:6px}
  .sector-list{list-style:none;left:88px;top:340px}
  .sector{display:flex;align-items:center;height:67px}
  .sector-icon{width:54px;height:54px;border-radius:50%;background:var(--cyan);display:flex;align-items:center;justify-content:center;flex:none}
  .sector-name{margin-left:16px;color:var(--white);font-size:17.5px;line-height:1.2;font-weight:400}

  /* photo hexes */
  .hex{position:absolute}
  .hex-right{left:408px;top:238px;width:420px;height:420px}
  .hex-left{left:7px;top:657px;width:400px;height:400px}

  /* content */
  .what{left:412px;top:664px;width:395px}
  .what h3{font-family:"Montserrat",sans-serif;font-weight:700;font-size:23px;color:var(--orange);line-height:1}
  .what p{margin-top:10px;font-size:15.5px;line-height:1.32;font-weight:500}
  .quote{left:412px;top:794px;width:390px;height:80px;border:1px solid #b9bcc7;padding:10px 16px;font-size:15.5px;line-height:1.32;font-weight:500}
  .quote-mark{left:587px;top:770px;width:40px;height:28px;background:var(--paper);text-align:center;font-family:"Montserrat",sans-serif;font-weight:800;font-size:40px;line-height:40px;color:#33334a}
  .cite{left:412px;top:882px;font-family:"Montserrat",sans-serif;font-weight:700;font-size:16.5px;line-height:1.35}
  .cite .who{color:var(--navy)}
  .cite .org{color:var(--orange)}
  .cta{right:18px;top:936px;text-align:right;font-family:"Montserrat",sans-serif}
  .cta .l1{font-size:23px;font-weight:800;color:var(--navy);line-height:1.1}
  .cta .l2{font-size:35px;font-weight:800;color:var(--orange);line-height:1.05}
  .cta .l3{font-family:"Quicksand",sans-serif;font-size:20px;font-weight:500;color:var(--navy);line-height:1.25}

  /* client names */
  .clients{left:36px;top:1062px;width:764px;display:flex;align-items:center;justify-content:space-between;gap:12px;
    font-family:"Montserrat",sans-serif;font-weight:700;font-size:13px;color:var(--navy)}
  .client{display:flex;align-items:center;gap:5px;white-space:nowrap}
  .client .dot{width:9px;height:9px;border-radius:50%;background:var(--orange)}

  /* footer */
  .web{left:88px;top:1121px;font-family:"Montserrat",sans-serif;font-size:15px;letter-spacing:3px;color:var(--white);display:flex;align-items:center;gap:12px}
  .web .dot{width:18px;height:18px;border-radius:50%;background:var(--orange)}
  .contact{right:20px;top:1121px;font-family:"Montserrat",sans-serif;font-weight:800;font-size:17px;letter-spacing:3px;color:var(--white)}
</style>
</head>
<body>
<main class="flyer">
  <svg class="backdrop" viewBox="0 0 820 1160" width="820" height="1160" aria-hidden="true">
    <defs>
      <linearGradient id="panelGrad" x1="0" y1="0" x2="1" y2="1">
        <stop offset="0" stop-color="#2a3aa8"/>
        <stop offset="1" stop-color="#3b52cf"/>
      </linearGradient>
      <linearGradient id="navyGrad" x1="0" y1="0" x2="1" y2="0">
        <stop offset="0" stop-color="#1f1a6c"/>
        <stop offset="1" stop-color="#262080"/>
      </linearGradient>
    </defs>
    <rect width="820" height="1160" fill="#f1f2f5"/>
    <polygon points="0,0 820,0 820,650 379,491 379,340 0,124" fill="url(#navyGrad)"/>
    <polygon points="0,124 379,340 379,760 42,980 42,358 0,334" fill="url(#panelGrad)"/>
    <rect x="0" y="1119" width="820" height="30" fill="var(--orange)"/>
    <polygon points="76,1119 430,1119 416,1149 62,1149" fill="var(--navy)"/>
    <rect x="0" y="1149" width="820" height="11" fill="var(--navy)"/>
  </svg>
  <svg class="abs" style="left:460px;top:120px" width="360" height="420" viewBox="0 0 360 420" role="img" aria-label="Faint photo of a glass office tower in the evening">
    <defs>
      <linearGradient id="towerGrad" x1="0" y1="0" x2="1" y2="1">
        <stop offset="0" stop-color="#2a2488" stop-opacity="0"/>
        <stop offset="1" stop-color="#3a33a0" stop-opacity=".55"/>
      </linearGradient>
    </defs>
    <rect width="360" height="420" fill="url(#towerGrad)"/>
  </svg>

  <div class="abs brand-mark"></div>
  <div class="abs brand-name">TalentBridge</div>
  <div class="abs brand-tag">Human Resources &amp; Recruitment</div>

  <header class="abs headline">
    <p class="lead">WE HAVE OVER <em>20 YEARS</em> OF</p>
    <p class="big">EXPERIENCE</p>
    <p class="sub">Helping companies hire<br>amazing talent</p>
  </header>

  <section class="abs industries">
    <h2>INDUSTRIES <span>WE SERVE</span></h2>
    <div class="rule"></div>
  </section>
  <ul class="abs sector-list">
    <li class="sector">
      <span class="sector-icon"><svg width="30" height="30" viewBox="0 0 30 30" fill="none" stroke="#fff" stroke-width="1.6"><path d="M4 26h22M8 26V12h6v14M17 26V6h5v20M8 16h6M17 11h5M17 16h5"/></svg></span>
      <span class="sector-name">Mining and<br>Oil &amp; Gas</span>
    </li>
    <li class="sector">
      <span class="sector-icon"><svg width="30" height="30" viewBox="0 0 30 30" fill="none" stroke="#fff" stroke-width="1.6"><rect x="6" y="4" width="18" height="22" rx="2"/><path d="M10 9h10M10 14h3M15 14h3M10 18h3M15 18h3M10 22h3M15 22h3"/></svg></span>
      <span class="sector-name">Accounting<br>&amp; Finance</span>
    </li>
    <li class="sector">
      <span class="sector-icon"><svg width="30" height="30" viewBox="0 0 30 30" fill="none" stroke="#fff" stroke-width="1.6"><path d="M5 12v6h4l10 6V6L9 12H5zM9 18l2 7h3l-2-7M23 11c2 1 2 7 0 8"/></svg></span>
      <span class="sector-name">Sales &amp;<br>Marketing</span>
    </li>
    <li class="sector">
      <span class="sector-icon"><svg width="30" height="30" viewBox="0 0 30 30" fill="none" stroke="#fff" stroke-width="1.6"><path d="M3 5h16v10H9l-4 4v-4H3zM12 18v3h10l4 4v-4h1V11h-4"/></svg></span>
      <span class="sector-name">IT &amp;<br>Communications</span>
    </li>
    <li class="sector">
      <span class="sector-icon"><svg width="30" height="30" viewBox="0 0 30 30" fill="none" stroke="#fff" stroke-width="1.6"><path d="M4 26h22M6 26V12h18v14M9 12l6-6 6 6M15 3v3M9 16h3v3H9zM18 16h3v3h-3zM9 21h3v3H9zM18 21h3v3h-3z"/></svg></span>
      <span class="sector-name">Government &amp;<br>Not for Profit</span>
    </li>
  </ul>

  <svg class="hex hex-right" viewBox="0 0 420 420" role="img" aria-label="Photo of a businesswoman in a meeting, framed in a hexagon">
    <defs>
      <linearGradient id="meetGrad" x1="0" y1="0" x2="1" y2="1">
        <stop offset="0" stop-color="#dfe2e6"/>
        <stop offset=".55" stop-color="#8d97b8"/>
        <stop offset="1" stop-color="#2a3358"/>
      </linearGradient>
      <linearGradient id="silver" x1="0" y1="0" x2="1" y2="1">
        <stop offset="0" stop-color="#ffffff"/>
        <stop offset=".5" stop-color="#a9adb7"/>
        <stop offset="1" stop-color="#f4f4f6"/>
      </linearGradient>
    </defs>
    <polygon points="210,2 390,106 390,314 210,418 30,314 30,106" fill="#2b39a8"/>
    <polygon points="210,27 368.5,118.5 368.5,301.5 210,393 51.5,301.5 51.5,118.5" fill="url(#silver)"/>
    <polygon points="210,38 359,124 359,296 210,382 61,296 61,124" fill="url(#meetGrad)"/>
  </svg>

  <svg class="hex hex-left" viewBox="0 0 400 400" role="img" aria-label="Photo of a businessman in a suit giving a thumbs up, framed in a hexagon">
    <defs>
      <linearGradient id="thumbGrad" x1="0" y1="0" x2="1" y2="1">
        <stop offset="0" stop-color="#2b3348"/>
        <stop offset=".5" stop-color="#c99a7f"/>
        <stop offset="1" stop-color="#1e2536"/>
      </linearGradient>
      <linearGradient id="silver2" x1="0" y1="0" x2="1" y2="1">
        <stop offset="0" stop-color="#ffffff"/>
        <stop offset=".5" stop-color="#a9adb7"/>
        <stop offset="1" stop-color="#f4f4f6"/>
      </linearGradient>
    </defs>
    <polygon points="200,5 368.9,102.5 368.9,297.5 200,395 31.1,297.5 31.1,102.5" fill="var(--sky)"/>
    <polygon points="200,28 349,114 349,286 200,372 51,286 51,114" fill="url(#silver2)"/>
    <polygon points="200,38 340.3,119 340.3,281 200,362 59.7,281 59.7,119" fill="url(#thumbGrad)"/>
  </svg>

  <section class="abs what">
    <h3>WHAT WE DO</h3>
    <p>We aren’t a recruitment agency, we are an extension of your team. We become your very own HR &amp; Recruitment department to be called upon as and when needed.</p>
  </section>

  <blockquote class="abs quote">TalentBridge really delivered on their promise and far exceeded our expectations. Their fixed fee model saved us thousands</blockquote>
  <div class="abs quote-mark">“</div>
  <p class="abs cite"><span class="who">MARK ELLISON GENERAL MANAGER</span><br><span class="org">Harbour Ledger Financial</span></p>

  <section class="abs cta">
    <p class="l1">START A CONVERSATION TODAY</p>
    <p class="l2">AND SEE WHY THESE</p>
    <p class="l3">companies turn to us time and time again</p>
  </section>

  <div class="abs clients">
    <span class="client">Arrowfleet</span>
    <span class="client">KESTREL</span>
    <span class="client">Cobalt Ridge</span>
    <span class="client">Southern Ores</span>
    <span class="client">Harbour Ledger</span>
    <span class="client">Brenner Systems</span>
    <span class="client"><span class="dot"></span>Quarto</span>
  </div>

  <div class="abs web"><span class="dot"></span>www.talentbridgehr.com.au</div>
  <div class="abs contact">GET IN TOUCH WITH US</div>
</main>
</body>
</html>
```